Copperfox Billboard

Please design a billboard using my photos and logos.
For photo of truck please crop the truck itself out and not have the trees / dirt in photo.
Please put " Best Prices in Sevier County"
Please put " 30-yard Dumpsters Starting at 600.00"
Please put " 16-yard Dumpsters Starting at 300.0"
Please put " Delivery and Pickup 7 Days a week"
Billboard size will be 10 ft tall 30 ft wide

```html
<!DOCTYPE html>
<html lang="en">
<head>
<meta charset="utf-8">
<title>Copperfox Dumpsters Billboard</title>
<link rel="stylesheet" href="https://fonts.googleapis.com/css2?family=Archivo+Black&family=Archivo:wght@600;700;800&display=swap">
<style>
  :root{
    --canvas:#000;
    --ink:#0a0a0a;
    --white:#fff;
    --red:#e00000;
    --red-dark:#8e0000;
    --lilac:#b86fc9;
    --plum:#640064;
    --plum-dark:#3a003c;
    --orchid:#c070cc;
    --silver-top:#d2d2d4;
    --silver-bottom:#fbfbfb;
    --violet-top:#c98ad0;
    --violet-bottom:#fcf8fc;
    --truck-a:#e9e9ec;
    --truck-b:#b9b9c0;
    --truck-c:#3e1a52;
  }
  *{box-sizing:border-box;margin:0;padding:0}
  html,body{width:1200px;height:1200px;overflow:hidden;background:var(--canvas)}
  body{position:relative;font-family:"Archivo",Arial,sans-serif}

  .billboard{position:absolute;left:59px;width:1087px;overflow:hidden}
  .billboard--silver{top:143px;height:374px;background:linear-gradient(180deg,var(--silver-top),var(--silver-bottom));
    --accent:var(--red);--accent-dark:var(--red-dark);--tag:var(--red);--best:var(--red);--price:var(--red);--icon:var(--red);
    --t-logo:25px;--t-web:46px;--t-mail:67px;--t-phone:34px;--t-h1:126px;--t-h2:185px;--t-box:141px;--h-box:69px;--t-best:268px;--t-l1:303px;--t-l2:329px;--t-truck:130px;--h-truck:232px}
  .billboard--violet{top:634px;height:409px;background:linear-gradient(180deg,var(--violet-top),var(--violet-bottom));
    --accent:var(--plum);--accent-dark:var(--plum-dark);--tag:var(--plum);--best:var(--orchid);--price:var(--plum);--icon:var(--white);
    --t-logo:31px;--t-web:51px;--t-mail:74px;--t-phone:42px;--t-h1:139px;--t-h2:204px;--t-box:154px;--h-box:76px;--t-best:294px;--t-l1:330px;--t-l2:360px;--t-truck:143px;--h-truck:257px}

  .brand{position:absolute;left:59px;top:var(--t-logo);display:flex;align-items:center;gap:8px;
    font-family:"Archivo Black",Arial,sans-serif;font-size:27px;line-height:1;color:var(--plum)}
  .brand__mark{width:14px;height:14px;background:var(--plum)}

  .contact{position:absolute;left:311px;display:flex;align-items:center;gap:8px;font-weight:700;font-size:12.5px;letter-spacing:.06em;color:var(--ink)}
  .contact svg{width:14px;height:14px}
  .contact--web{top:var(--t-web)}
  .contact--mail{top:var(--t-mail)}

  .phone{position:absolute;left:609px;top:var(--t-phone);display:flex;align-items:center;gap:12px}
  .phone svg{width:50px;height:50px}
  .phone__number{font-family:"Archivo Black",Arial,sans-serif;font-size:56px;line-height:1;color:var(--ink);letter-spacing:-.01em}

  .truck-photo{position:absolute;left:12px;top:var(--t-truck);width:364px;height:var(--h-truck);
    border-radius:40px 30px 60px 80px;background:radial-gradient(ellipse at 35% 45%,var(--truck-a) 0%,var(--truck-b) 55%,transparent 75%),
    linear-gradient(90deg,transparent 55%,var(--truck-c) 70%,transparent 98%);opacity:.95}

  .headline{position:absolute;font-family:"Archivo Black",Arial,sans-serif;line-height:1;letter-spacing:-.01em;
    background:linear-gradient(180deg,var(--accent) 0%,var(--accent-dark) 55%,var(--accent) 100%);
    -webkit-background-clip:text;background-clip:text;color:transparent;filter:drop-shadow(3px 4px 3px rgba(0,0,0,.25))}
  .headline--one{left:254px;top:var(--t-h1);font-size:74px}
  .headline--two{left:295px;top:var(--t-h2);font-size:74px}

  .tag{position:absolute;left:769px;top:var(--t-box);width:318px;height:var(--h-box);background:var(--tag);color:var(--white);
    padding-left:23px;display:flex;flex-direction:column;justify-content:center;font-weight:800;text-transform:uppercase}
  .tag::after{content:"";position:absolute;left:0;right:0;bottom:-12px;height:9px;background:var(--lilac)}
  .tag__small{font-size:18.5px;letter-spacing:.02em;line-height:1.1}
  .tag__big{font-family:"Archivo Black",Arial,sans-serif;font-size:30px;line-height:1.05;letter-spacing:.02em}

  .best{position:absolute;left:396px;top:var(--t-best);font-family:"Archivo Black",Arial,sans-serif;font-size:28px;letter-spacing:.045em;color:var(--best);text-transform:uppercase}
  .offer{position:absolute;left:396px;font-weight:800;font-size:20.5px;letter-spacing:.06em;color:var(--ink);text-transform:uppercase;white-space:nowrap}
  .offer--30{top:var(--t-l1)}
  .offer--16{top:var(--t-l2)}
  .offer__price{font-family:"Archivo Black",Arial,sans-serif;font-size:25px;color:var(--price);margin-left:6px}
</style>
</head>
<body>

<section class="billboard billboard--silver">
  <div class="brand"><span class="brand__mark"></span>Copperfox</div>
  <div class="contact contact--web">
    <svg viewBox="0 0 16 16" fill="none" stroke="#111" stroke-width="1.2"><circle cx="8" cy="8" r="6.5"/><ellipse cx="8" cy="8" rx="3" ry="6.5"/><path d="M1.5 8h13M2.5 4.7h11M2.5 11.3h11"/></svg>
    www.copperfoxdumpsters.com</div>
  <div class="contact contact--mail">
    <svg viewBox="0 0 16 16" fill="none" stroke="#111" stroke-width="1.2"><rect x="1" y="3" width="14" height="10"/><path d="M1 3l7 6 7-6M1 13l5-5M15 13l-5-5"/></svg>
    info@copperfoxdumpsters.com</div>
  <div class="phone">
    <svg viewBox="0 0 50 50" fill="none" stroke="var(--icon)" stroke-width="3.2" stroke-linecap="round" stroke-linejoin="round"><path d="M9 6l7-2 6 10-4 4c2 6 7 11 13 13l4-4 10 6-2 7c-2 3-6 4-10 2C20 37 13 30 8 17 6 13 6 8 9 6z"/><path d="M28 13a9 9 0 0 1 9 9M29 6a16 16 0 0 1 15 15M28 19a3 3 0 0 1 3 3"/></svg>
    <span class="phone__number">865-555-0142</span>
  </div>
  <div class="truck-photo" role="img" aria-label="Photo of a white roll-off truck carrying a purple dumpster, cut out from its background"></div>
  <h1 class="headline headline--one">DUMPSTER</h1>
  <div class="headline headline--two">RENTALS</div>
  <div class="tag"><span class="tag__small">Delivery and Pickup</span><span class="tag__big">7 Days a Week</span></div>
  <div class="best">Best Prices in Sevier County</div>
  <div class="offer offer--30">30-Yard Dumpsters Starting at<span class="offer__price">$600.00</span></div>
  <div class="offer offer--16">16-Yard Dumpsters Starting at<span class="offer__price">$300.00</span></div>
</section>

<section class="billboard billboard--violet">
  <div class="brand"><span class="brand__mark"></span>Copperfox</div>
  <div class="contact contact--web">
    <svg viewBox="0 0 16 16" fill="none" stroke="#111" stroke-width="1.2"><circle cx="8" cy="8" r="6.5"/><ellipse cx="8" cy="8" rx="3" ry="6.5"/><path d="M1.5 8h13M2.5 4.7h11M2.5 11.3h11"/></svg>
    www.copperfoxdumpsters.com</div>
  <div class="contact contact--mail">
    <svg viewBox="0 0 16 16" fill="none" stroke="#111" stroke-width="1.2"><rect x="1" y="3" width="14" height="10"/><path d="M1 3l7 6 7-6M1 13l5-5M15 13l-5-5"/></svg>
    info@copperfoxdumpsters.com</div>
  <div class="phone">
    <svg viewBox="0 0 50 50" fill="none" stroke="var(--icon)" stroke-width="3.2" stroke-linecap="round" stroke-linejoin="round"><path d="M9 6l7-2 6 10-4 4c2 6 7 11 13 13l4-4 10 6-2 7c-2 3-6 4-10 2C20 37 13 30 8 17 6 13 6 8 9 6z"/><path d="M28 13a9 9 0 0 1 9 9M29 6a16 16 0 0 1 15 15M28 19a3 3 0 0 1 3 3"/></svg>
    <span class="phone__number">865-555-0142</span>
  </div>
  <div class="truck-photo" role="img" aria-label="Photo of a white roll-off truck carrying a purple dumpster, cut out from its background"></div>
  <div class="headline headline--one">DUMPSTER</div>
  <div class="headline headline--two">RENTALS</div>
  <div class="tag"><span class="tag__small">Delivery and Pickup</span><span class="tag__big">7 Days a Week</span></div>
  <div class="best">Best Prices in Sevier County</div>
  <div class="offer offer--30">30-Yard Dumpsters Starting at<span class="offer__price">$600.00</span></div>
  <div class="offer offer--16">16-Yard Dumpsters Starting at<span class="offer__price">$300.00</span></div>
</section>

</body>
</html>
```